Visitenkarten-Design für Immobilienmakler
Zielgruppe
Immobilienmakler
Aufgabenstellung
Top moderne hochwertige Visitenkate, wir hätten gerne eine sehr hochwertig moderne Visitenkarte mit Bild vom Mitarbeiter... Anbei habe ich die alte Visitenkarte die ich sehr kindlich finde... Es sollte jetzt sehr exklusive aussehen. Alle Daten können von der alten Visitenkarte übernommen werden.. danke

```html
<!DOCTYPE html>
<html lang="de">
<head>
<meta charset="utf-8">
<title>Visitenkarte – Velmar Agentur</title>
<link rel="stylesheet" href="https://fonts.googleapis.com/css2?family=Oswald:wght@400;500;600&display=swap">
<style>
  :root {
    --page-bg: #ffffff;
    --card-light: #f1f3f7;
    --card-dark: #3a3a3a;
    --ink: #2b2b2b;
    --ink-soft: #3c3c3c;
    --rule: #5a5a5a;
    --name-light: #e9e9e9;
    --photo-a: #dfe4ea;
    --photo-b: #b9a593;
  }
  * { box-sizing: border-box; margin: 0; padding: 0; }
  html, body { width: 1200px; height: 1200px; overflow: hidden; background: var(--page-bg); }
  .canvas { position: relative; width: 1200px; height: 1200px; }

  .card {
    position: absolute;
    top: 427px;
    width: 546px;
    height: 346px;
    box-shadow: 0 2px 6px rgba(0,0,0,0.18);
  }
  .card--front { left: 26px; background: var(--card-light); color: var(--ink); }
  .card--back  { left: 628px; background: var(--card-dark); }

  .portrait {
    position: absolute; left: 15px; top: 15px;
    width: 180px; height: 180px; border-radius: 50%;
    background: radial-gradient(circle at 50% 40%, var(--photo-b) 0 28%, var(--photo-a) 60%);
  }

  .company-name {
    position: absolute;
    font-family: 'Oswald', sans-serif;
    font-weight: 500;
    line-height: 1;
    white-space: nowrap;
  }
  .card--front .company-name { right: 22px; top: 40px; font-size: 36px; color: var(--ink-soft); }
  .card--back  .company-name {
    left: 0; right: 0; top: 143px;
    text-align: center; font-size: 52px; color: var(--name-light);
  }

  .person {
    position: absolute; left: 0; width: 229px; top: 232px;
    text-align: center; font-family: 'Oswald', sans-serif;
  }
  .person__name { font-size: 20px; font-weight: 600; margin-bottom: 16px; }
  .person__address { font-size: 14.5px; font-weight: 400; line-height: 19px; }

  .divider {
    position: absolute; left: 229px; top: 228px;
    width: 1px; height: 91px; background: var(--rule);
  }

  .contact {
    position: absolute; left: 312px; right: 36px; top: 238px;
    list-style: none; font-family: 'Oswald', sans-serif; font-size: 14px;
  }
  .contact li {
    display: flex; align-items: center; justify-content: space-between;
    height: 19px;
  }
  .contact svg { width: 12px; height: 12px; fill: var(--ink); }
</style>
</head>
<body>
<main class="canvas">
  <section class="card card--front" aria-label="Visitenkarte Vorderseite">
    <div class="portrait" role="img" aria-label="Porträtfoto des Mitarbeiters"></div>
    <div class="company-name">Velmar Agentur</div>

    <div class="person">
      <p class="person__name">Lukas Brandner</p>
      <p class="person__address">Am Feldweg 12<br>6850 Dornau</p>
    </div>

    <div class="divider"></div>

    <ul class="contact">
      <li>
        <svg viewBox="0 0 24 24" aria-hidden="true"><path d="M6.6 10.8a15.1 15.1 0 0 0 6.6 6.6l2.2-2.2c.3-.3.7-.4 1-.2 1.1.4 2.3.6 3.6.6.6 0 1 .4 1 1V20c0 .6-.4 1-1 1A17 17 0 0 1 3 4c0-.6.4-1 1-1h3.5c.6 0 1 .4 1 1 0 1.3.2 2.5.6 3.6.1.3 0 .7-.2 1z"/></svg>
        <span>+43 5500 12 345 67</span>
      </li>
      <li>
        <svg viewBox="0 0 24 24" aria-hidden="true"><path d="M7 1h10a2 2 0 0 1 2 2v18a2 2 0 0 1-2 2H7a2 2 0 0 1-2-2V3a2 2 0 0 1 2-2zm0 3v14h10V4zm5 15.2a1 1 0 1 0 0 2 1 1 0 0 0 0-2z"/></svg>
        <span>+43 660 1234 567</span>
      </li>
      <li>
        <svg viewBox="0 0 24 24" aria-hidden="true"><path d="M12 2a10 10 0 1 0 5 18.7l-1-1.7A8 8 0 1 1 20 12v1.2c0 1-.7 1.8-1.5 1.8S17 14.2 17 13.2V7h-2v1a5 5 0 1 0 .5 7 3.4 3.4 0 0 0 3 2c2 0 3.5-1.7 3.5-3.8V12A10 10 0 0 0 12 2zm0 13a3 3 0 1 1 0-6 3 3 0 0 1 0 6z"/></svg>
        <span>lukas@velmar-agentur.com</span>
      </li>
      <li>
        <span></span>
        <span>www.velmar-agentur.com</span>
      </li>
    </ul>
  </section>

  <section class="card card--back" aria-label="Visitenkarte Rückseite">
    <div class="company-name">Velmar Agentur</div>
  </section>
</main>
</body>
</html>
```